Elegant and modern Wedding Photography brochure

My existing brochure (attached) needs a major facelift. This is one of the main selling tools - it gets emailed to my clients when they make an equiry on what packages i offer and it is printed out and walked through at our first meeting. This brochure is as critical as my website - it needs to sing!

I'm looking for an eye-catching design that says:
Elegant
Modern
Clean
Crisp
Not cutesy or lovey-dovey thanks - we are more sophisticated and professional than that.

Update images to some of the latest weddings I've shot also. Let me know files and resolution you need. I've enabled right-click to download images on my site for a limited time. Please note that I retain copyright and will pursue any breeches.

Http://www.carlathornbey.com/Melbourne-wedding-photography
Updates

Thanks for all of your designs! Will take a few days to decide.

Target Market(s)

Australian Women aged 24-44

Industry/Entity Type

Wedding

Font styles to use
Other font styles liked:
• Century Gothic

Requirements
Must have
• Easy to print - does not have to be 6 A4 pages like the existing brochure
Nice to have
• Some full page images - The photos are supposed to be the hero here :-)
Should not have
• Not cutesy or lovey-dovey thanks - we are more sophisticated and professional than that.

No black backgrounds, I prefer a white thanks

No images in organic shaped boxes (like the rectangles in the logo - no thanks).
Keep the lines straight and sharp

```html
<!DOCTYPE html>
<html lang="en">
<head>
<meta charset="utf-8">
<title>Wedding Packages – Pricelist 2014</title>
<link rel="stylesheet" href="https://fonts.googleapis.com/css2?family=Didact+Gothic&family=Questrial&display=swap">
<style>
:root{
  --plum:#8a2f84;
  --plum-text:#8b3a88;
  --lilac:#e6d2e6;
  --lilac-line:#c9a9c8;
  --ink:#1f1f1f;
  --rule:#d9d9d9;
  --paper:#ffffff;
  --surround:#262626;
  --photo-warm:linear-gradient(160deg,#8c7a4a 0%,#b9a77a 35%,#e9e6e2 60%,#6f6a4a 100%);
  --photo-mono:linear-gradient(170deg,#4a4a4a 0%,#9a9a9a 40%,#d8d8d8 65%,#3a3a3a 100%);
}
*{box-sizing:border-box;margin:0;padding:0}
html,body{width:1200px;height:857px;overflow:hidden}
body{background:var(--surround);font-family:"Didact Gothic",sans-serif;color:var(--ink);position:relative}
.page-tag{position:absolute;top:4px;color:#e8e8e8;font-family:"Questrial",sans-serif;font-size:13px}
.page-tag--left{left:22px}.page-tag--right{right:22px}
.spread{position:absolute;left:27px;top:22px;width:1147px;height:812px;background:var(--paper);overflow:hidden}
.spine{position:absolute;left:573px;top:0;width:1px;height:100%;background:#bdbdbd}
.rule-top,.rule-bottom{position:absolute;left:0;width:100%;height:1px;background:var(--plum)}
.rule-top{top:44px}.rule-bottom{top:101px}
.header-band{position:absolute;left:0;top:48px;width:100%;height:48px;background:var(--plum)}
.page-title{position:absolute;top:50px;color:#fff;font-family:"Questrial",sans-serif;font-weight:400;font-size:25px;line-height:44px}
.page-title small{font-size:17px}
.page-title--left{left:36px}.page-title--right{left:609px}
.diamonds{position:absolute;left:0;top:0}
.divider-h{position:absolute;height:1px;background:var(--rule)}
.package{position:absolute;top:336px;width:160px}
.package__head{height:35px;background:var(--lilac);text-align:center;color:var(--plum-text)}
.package__name{font-family:"Questrial",sans-serif;font-size:12.5px;padding-top:3px}
.package__price{font-size:8px;margin-top:2px}
.package__list{list-style:none;margin-top:17px;padding-left:2px;width:150px}
.package__list li{font-size:8.8px;line-height:13.5px;padding-left:9px;position:relative;margin-bottom:7.5px}
.package__list li::before{content:"";position:absolute;left:0;top:5px;width:3px;height:3px;border-radius:50%;background:var(--ink)}
.divider-v{position:absolute;top:336px;width:1px;height:323px;background:var(--rule)}
.footnote{position:absolute;left:24px;top:675px;font-size:6.5px;color:var(--plum-text)}
.footer-band{position:absolute;top:796px;height:16px;background:var(--lilac)}
.footer-band--left{left:0;width:573px}.footer-band--right{left:574px;width:573px}
.page-num{position:absolute;top:797px;width:15px;height:14px;background:var(--plum);color:#fff;font-size:8px;text-align:center;line-height:14px}
.photo{position:absolute}
.photo--bridal{left:607px;top:126px;width:253px;height:367px;background:var(--photo-warm)}
.photo--veil{left:607px;top:502px;width:253px;height:248px;background:var(--photo-mono)}
.fees{position:absolute;left:869px;top:126px;width:243px;height:624px;background:var(--lilac);padding:22px 12px 0 12px;overflow:hidden}
.fee{border-bottom:1px solid var(--lilac-line);padding:3px 0 6px;font-size:8.6px;line-height:13px}
.fee:last-child{border-bottom:none}
.fee + .fee{padding-top:8px}
.fee__name{font-weight:700;font-family:"Questrial",sans-serif;-webkit-text-stroke:.25px var(--ink)}
.fee ul{list-style:none}
.fee li{position:relative;padding-left:12px;margin-top:3px}
.fee li::before{content:"";position:absolute;left:3px;top:5px;width:3px;height:3px;border-radius:50%;background:var(--ink)}
</style>
</head>
<body>
<span class="page-tag page-tag--left">Pg-3</span>
<span class="page-tag page-tag--right">Pg-4</span>

<main class="spread">
  <div class="rule-top"></div>
  <div class="header-band"></div>
  <div class="rule-bottom"></div>
  <div class="spine"></div>

  <h1 class="page-title page-title--left">Wedding Packages <small>(Pricelist 2014)</small></h1>
  <h2 class="page-title page-title--right">À la Carte Fees to Consider</h2>

  <svg class="diamonds" width="573" height="330" viewBox="0 0 573 330">
    <defs>
      <linearGradient id="tone-a" x1="0" y1="0" x2="1" y2="1"><stop offset="0" stop-color="#6b6154"/><stop offset=".5" stop-color="#d8d2c8"/><stop offset="1" stop-color="#2d2b2a"/></linearGradient>
      <linearGradient id="tone-b" x1="0" y1="0" x2="1" y2="1"><stop offset="0" stop-color="#a88062"/><stop offset=".5" stop-color="#e9c7b2"/><stop offset="1" stop-color="#d9c6bd"/></linearGradient>
      <linearGradient id="tone-c" x1="0" y1="0" x2="1" y2="1"><stop offset="0" stop-color="#7a8a4a"/><stop offset=".5" stop-color="#e4e2dc"/><stop offset="1" stop-color="#3a3a30"/></linearGradient>
    </defs>
    <polygon role="img" aria-label="Photo of bride and groom in front of a stone wall" points="104,128 191,215 104,302 17,215" fill="url(#tone-a)" stroke="#d8c6d8"/>
    <polygon role="img" aria-label="Close portrait of a smiling bride" points="287,128 374,215 287,302 200,215" fill="url(#tone-b)" stroke="#d8c6d8"/>
    <polygon role="img" aria-label="Photo of bride and groom under willow trees" points="469,128 556,215 469,302 382,215" fill="url(#tone-c)" stroke="#d8c6d8"/>
  </svg>

  <div class="divider-h" style="left:24px;top:327px;width:525px"></div>

  <section class="package" style="left:24px">
    <div class="package__head"><div class="package__name">Signature</div><div class="package__price">Price: $3650 ($5540 value)</div></div>
    <ul class="package__list">
      <li>Up to 8 hrs of coverage</li>
      <li>Signature Grand (A3) Album with Lay-flat 300g paper, frosted page, choice of premium linen or leather cover, presentation box, name embossing, up to 52 pages</li>
      <li>Custom Thank-you Cards with envelopes (50)</li>
      <li>Client for life (no sitting fees)</li>
      <li>Second photographer</li>
      <li>Fusion Slideshow (still + moving images)</li>
      <li>Pre-wedding Shoot</li>
      <li>Web Gallery (online for 6 weeks) &amp; Social media</li>
      <li>High Resolution Digital Negatives*</li>
    </ul>
  </section>
  <div class="divider-v" style="left:195px"></div>

  <section class="package" style="left:207px">
    <div class="package__head"><div class="package__name">Platinum</div><div class="package__price">Price: $2300 ($3440 value)</div></div>
    <ul class="package__list">
      <li>Up to 6 hrs of coverage</li>
      <li>Regular (A4) Album with Lay-flat 300g paper, printed cover, dust jacket, presentation box, up to 42 pages</li>
      <li>Slideshow</li>
      <li>Pre-wedding shoot</li>
      <li>Web Gallery (online for 6 weeks) &amp; Social media</li>
      <li>High Resolution Digital Negatives*</li>
    </ul>
  </section>
  <div class="divider-v" style="left:378px"></div>

  <section class="package" style="left:390px">
    <div class="package__head"><div class="package__name">Gold</div><div class="package__price">Price: $1650 ($2080 value)</div></div>
    <ul class="package__list">
      <li>Up to 4 hrs of coverage</li>
      <li>Regular (A4) Album with Lay-flat 300g paper, printed cover, dust jacket, presentation box, up to 32 pages</li>
      <li>Web Gallery (online for 6 weeks) &amp; Social media</li>
      <li>High Resolution Digital Negatives*</li>
    </ul>
  </section>

  <div class="divider-h" style="left:24px;top:670px;width:525px"></div>
  <p class="footnote">* Approx. 1200x1800 jpeg at 240 pixels per inch. Suitable for prints up to 8x10 inch. No watermarks</p>
  <div class="divider-h" style="left:24px;top:691px;width:525px"></div>

  <div class="photo photo--bridal" role="img" aria-label="Laughing bride with bouquet and bridesmaid under autumn willow"></div>
  <div class="photo photo--veil" role="img" aria-label="Black and white portrait of bride in a lace veil looking down"></div>

  <aside class="fees">
    <div class="fee"><div class="fee__name">Engagement Session/Pre-wedding Shoot:</div>$290 for up to 2 hours of photography on location</div>
    <div class="fee"><div class="fee__name">Digital Negatives:</div>$490</div>
    <div class="fee"><div class="fee__name">Extended Coverage:</div>$160 per hour</div>
    <div class="fee"><div class="fee__name">Web Gallery &amp; Sharelane posting:</div>$160</div>
    <div class="fee"><div class="fee__name">Slideshow:</div>$250</div>
    <div class="fee"><div class="fee__name">Second Photographer:</div>$590</div>
    <div class="fee"><div class="fee__name">Client for life:</div>No sitting fees for portrait sessions – Anniversaries, family portraits, etc: $390</div>
    <div class="fee"><div class="fee__name">Photo Enlargements:</div>
      <ul>
        <li>Quality custom archival prints in a variety of sizes 5x7 up to 8x10 $25, 12.5x18.5 $50</li>
        <li>Stretched Canvas Prints for your wall Various sizes available from 16"x20" starting at $395 through to 60"x96" $1500</li>
        <li>Plus many other options!</li>
      </ul>
    </div>
    <div class="fee"><div class="fee__name">Professionally Edited Album (Regular):</div>$790</div>
    <div class="fee"><div class="fee__name">Album Upgrade from Regular to Signature Grand:</div>
      <ul>
        <li>From Gold Package to Signature Grand: $1150</li>
        <li>From Platinum Package to Signature Grand: $650</li>
      </ul>
    </div>
    <div class="fee"><div class="fee__name">Custom Thank-you Cards:</div>$150 for 50 cards (174mm x 123mm) including envelopes</div>
  </aside>

  <div class="footer-band footer-band--left"></div>
  <div class="footer-band footer-band--right"></div>
  <div class="page-num" style="left:3px">3</div>
  <div class="page-num" style="left:1129px">4</div>
</main>
</body>
</html>
```